Design graphics and Print for a line of Herb Seeds- Envelope Design

We need a set of herb seed envelopes designed for a new seed line we are launching.
The design will be both front and back

Envelope will be a colored ( green) ) envelope with white text
or a white or cream envelope in all black /and images text. Or can add some colors to the white envelope.

I have attached the die-cut of the seed envelope.
I have attached some images of envelopes I like. Please do not copy, these are just to give you an idea of what I like.

Please feel free to reach out to me if you have any questions.

Thank you

Target Market(s)

The design needs to classic that can translate to 3 different audiences. 1. young parents 2. hip, young single millennial 3. kids

Industry/Entity Type

Ecommerce

Font styles to use
Serif

Requirements
Must have
• Please use the herb - Parsley for the design
Icon, Text or both.

Front side must have:
1.either herb Icon or work Parsley or both- this will be the main attraction
2. company name- Tall Meadow Pantry
3. can use design elements
4. can use my logo on from or back or not at all. I

Backside must have:
1. social media tags
FB, Instagram and Pinterest ( use icons) @tallmeadowpantry

my website: www.tallmeadowpantry.example
this can be on from or back of the envelope.
Should not have
• please stay away from "county" flowery, old fashioned style designs

```html
<!DOCTYPE html>
<html lang="en">
<head>
<meta charset="utf-8">
<title>Tall Meadow Pantry — Parsley Seed Envelope</title>
<link rel="stylesheet" href="https://fonts.googleapis.com/css2?family=Josefin+Sans:wght@100;300;400;600&display=swap">
<style>
  :root {
    --page: #ffffff;
    --cream: #f8f9e6;
    --cream-fold: #eef0d8;
    --sage: #979b72;
    --sage-fold: #8c9068;
    --ink: #1c1c1a;
    --paper-white: #ffffff;
    --type: "Josefin Sans", sans-serif;
  }
  * { box-sizing: border-box; margin: 0; padding: 0; }
  html, body { width: 1200px; height: 1200px; overflow: hidden; background: var(--page); }
  .sheet {
    position: relative; width: 1200px; height: 1200px;
    display: grid; grid-template-columns: 400px 400px; grid-template-rows: 500px 500px;
    gap: 40px 60px; justify-content: center; align-content: center;
    font-family: var(--type);
  }
  .envelope { position: relative; overflow: hidden; }
  .envelope--cream { background: var(--cream); color: var(--ink); --fold: var(--cream-fold); --line: rgba(0,0,0,.12); }
  .envelope--sage { background: var(--sage); color: var(--paper-white); --fold: var(--sage-fold); --line: rgba(0,0,0,.1); }

  /* front */
  .brand {
    position: absolute; top: 38px; left: 0; right: 0; text-align: center;
    font-size: 15px; font-weight: 400; letter-spacing: .32em; text-transform: uppercase;
  }
  .rule { position: absolute; left: 50%; height: 1px; background: currentColor; transform: translateX(-50%); }
  .rule--top { top: 72px; width: 84px; }
  .rule--bottom { bottom: 42px; width: 120px; }
  .rule::after {
    content: ""; position: absolute; left: 50%; top: -3px; width: 7px; height: 7px;
    border-radius: 50%; background: currentColor; transform: translateX(-50%);
  }
  .emblem { position: absolute; top: 118px; left: 50%; transform: translateX(-50%); width: 196px; height: 196px; }
  .herb-name {
    position: absolute; top: 318px; right: 72px;
    font-size: 46px; font-weight: 300; letter-spacing: .01em;
  }

  /* back */
  .flaps { position: absolute; inset: 0; width: 100%; height: 100%; }
  .mark { position: absolute; right: 34px; bottom: 132px; display: flex; align-items: center; gap: 8px; }
  .mark-dot { width: 30px; height: 30px; border-radius: 50%; border: 1.5px solid currentColor; }
  .mark-name { font-size: 13px; font-weight: 400; letter-spacing: .08em; text-transform: uppercase; }
  .contact { position: absolute; right: 34px; bottom: 92px; text-align: right; font-size: 13px; font-weight: 400; line-height: 1.4; }
</style>
</head>
<body>
<main class="sheet">

  <!-- cream front -->
  <section class="envelope envelope--cream envelope-front">
    <p class="brand">Tall Meadow Pantry</p>
    <span class="rule rule--top"></span>
    <svg class="emblem" viewBox="0 0 196 196">
      <circle cx="98" cy="98" r="96" fill="none" stroke="currentColor" stroke-width="2"/>
      <circle cx="98" cy="98" r="90" fill="none" stroke="currentColor" stroke-width="1"/>
      <circle cx="98" cy="98" r="62" fill="#2a2a28" role="img" aria-label="Parsley leaf illustration"/>
    </svg>
    <p class="herb-name">parsley</p>
    <span class="rule rule--bottom"></span>
  </section>

  <!-- cream back -->
  <section class="envelope envelope--cream envelope-back">
    <svg class="flaps" viewBox="0 0 400 500" preserveAspectRatio="none">
      <path d="M0 0 H400 V40 Q400 56 384 58 H64 Q48 58 46 74 V500 H0 Z" fill="var(--fold)"/>
      <path d="M46 500 V395 Q48 380 64 380 H384 Q400 382 400 398 V500 Z" fill="var(--fold)"/>
      <path d="M46 74 V500 M64 58 H384 M64 380 H384" stroke="var(--line)" fill="none"/>
    </svg>
    <div class="mark"><span class="mark-dot"></span><span class="mark-name">Tall Meadow Pantry</span></div>
    <p class="contact">@tallmeadowpantry<br>www.tallmeadowpantry.example</p>
  </section>

  <!-- sage front -->
  <section class="envelope envelope--sage envelope-front">
    <p class="brand">Tall Meadow Pantry</p>
    <span class="rule rule--top"></span>
    <svg class="emblem" viewBox="0 0 196 196">
      <circle cx="98" cy="98" r="96" fill="none" stroke="currentColor" stroke-width="2"/>
      <circle cx="98" cy="98" r="90" fill="none" stroke="currentColor" stroke-width="1"/>
      <circle cx="98" cy="98" r="62" fill="#f4f4ec" role="img" aria-label="Parsley leaf illustration"/>
    </svg>
    <p class="herb-name">parsley</p>
    <span class="rule rule--bottom"></span>
  </section>

  <!-- sage back -->
  <section class="envelope envelope--sage envelope-back">
    <svg class="flaps" viewBox="0 0 400 500" preserveAspectRatio="none">
      <path d="M0 0 H400 V40 Q400 56 384 58 H64 Q48 58 46 74 V500 H0 Z" fill="var(--fold)"/>
      <path d="M46 500 V395 Q48 380 64 380 H384 Q400 382 400 398 V500 Z" fill="var(--fold)"/>
      <path d="M46 74 V500 M64 58 H384 M64 380 H384" stroke="var(--line)" fill="none"/>
    </svg>
    <div class="mark"><span class="mark-dot"></span><span class="mark-name">Tall Meadow Pantry</span></div>
    <p class="contact">@tallmeadowpantry<br>www.tallmeadowpantry.example</p>
  </section>

</main>
</body>
</html>
```